Marrowby Lane School bookmark

We need a vertical card (DL 99x210 mm) that will be put inside books at a primary school for children to make comments about the books. Text at the top:
Marrowby Lane School (and logo)
What did you think of this book?

Text at the bottom:
Pass it on!

Words in repeated pattern around the edge: funny sad exciting mysterious fantastic boring enthralling interesting

It should be in interesting bright colours with a white or pale background as children will write on the cards

The card should be double sided with the same design on each side

Industry/Entity Type

School

```html
<!DOCTYPE html>
<html lang="en">
<head>
<meta charset="utf-8">
<title>Marrowby Lane School – Book Card</title>
<link rel="stylesheet" href="https://fonts.googleapis.com/css2?family=Oswald:wght@600;700&family=Libre+Baskerville:wght@700&family=Lato:wght@700&display=swap">
<style>
  :root {
    --red: #c8202a;
    --red-bright: #e3242b;
    --red-deep: #a5161d;
    --blue: #1f3f8a;
    --white: #ffffff;
    --grey: #b9b9b9;
    --ink: #2a2a2a;
    --photo-sky: #f7f5f2;
    --photo-warm: #f3e7df;
    --photo-cool: #e6ebf3;
  }
  * { margin: 0; padding: 0; box-sizing: border-box; }
  html, body { width: 902px; height: 1200px; overflow: hidden; background: var(--white); }
  .card {
    position: relative;
    width: 902px;
    height: 1200px;
    overflow: hidden;
    background: var(--white);
  }
  .word-border {
    position: absolute;
    overflow: hidden;
    white-space: nowrap;
    font-family: "Oswald", "Arial Narrow", sans-serif;
    font-weight: 600;
    font-size: 16px;
    line-height: 32px;
    letter-spacing: 1px;
    text-transform: uppercase;
    color: var(--red);
  }
  .word-border span { margin: 0 7px; }
  .word-border span:nth-child(even) { color: var(--blue); }
  .word-border--top { left: 0; top: 0; width: 902px; height: 32px; text-align: center; }
  .word-border--left,
  .word-border--right {
    top: 32px; width: 32px; height: 938px;
    writing-mode: vertical-rl;
    text-align: center;
  }
  .word-border--left { left: 0; transform: rotate(180deg); }
  .word-border--right { right: 0; }
  .hero-photo {
    position: absolute;
    left: 32px; top: 32px;
    width: 838px; height: 938px;
    background:
      radial-gradient(ellipse at 62% 62%, rgba(227,36,43,0.10), transparent 55%),
      radial-gradient(ellipse at 28% 66%, rgba(31,63,138,0.10), transparent 50%),
      linear-gradient(180deg, var(--photo-sky) 0%, var(--photo-warm) 55%, var(--photo-cool) 100%);
  }
  .headline {
    position: absolute;
    left: 0; right: 0; top: 66px;
    text-align: center;
    font-family: "Oswald", "Arial Narrow", sans-serif;
    font-weight: 700;
    font-size: 68px;
    line-height: 1.25;
    color: var(--red);
    text-transform: uppercase;
  }
  .school-mark {
    position: absolute;
    left: 331px; top: 756px;
    width: 240px; height: 240px;
    border-radius: 50%;
    background: var(--white);
    border: 6px solid var(--red);
    display: flex;
    align-items: center;
    justify-content: center;
    text-align: center;
    padding: 30px;
    font-family: "Oswald", "Arial Narrow", sans-serif;
    font-weight: 600;
    font-size: 34px;
    line-height: 1.15;
    color: var(--red);
    text-transform: uppercase;
    z-index: 2;
  }
  .pass-band {
    position: absolute;
    left: 0; top: 978px;
    width: 902px; height: 124px;
    background: linear-gradient(90deg, var(--red-deep) 0%, var(--red-bright) 50%, var(--red-deep) 100%);
    display: flex;
    align-items: center;
    justify-content: center;
    padding-top: 14px;
    font-family: "Libre Baskerville", Georgia, serif;
    font-weight: 700;
    font-size: 56px;
    color: var(--white);
    letter-spacing: 1px;
  }
  .web-band {
    position: absolute;
    left: 0; top: 1110px;
    width: 902px; height: 90px;
    background: var(--grey);
    display: flex;
    align-items: center;
    justify-content: center;
    font-family: "Lato", Arial, sans-serif;
    font-weight: 700;
    font-size: 30px;
    color: var(--ink);
  }
</style>
</head>
<body>
  <main class="card">
    <div class="word-border word-border--top" aria-hidden="true"><span>funny</span><span>sad</span><span>exciting</span><span>mysterious</span><span>fantastic</span><span>boring</span><span>enthralling</span><span>interesting</span><span>funny</span><span>sad</span></div>
    <div class="word-border word-border--left" aria-hidden="true"><span>funny</span><span>sad</span><span>exciting</span><span>mysterious</span><span>fantastic</span><span>boring</span><span>enthralling</span><span>interesting</span><span>funny</span><span>sad</span><span>exciting</span></div>
    <div class="word-border word-border--right" aria-hidden="true"><span>funny</span><span>sad</span><span>exciting</span><span>mysterious</span><span>fantastic</span><span>boring</span><span>enthralling</span><span>interesting</span><span>funny</span><span>sad</span><span>exciting</span></div>
    <div class="hero-photo" role="img" aria-label="Pale photograph of smiling pupils in red school jumpers and blue coats running across a playground past painted wall murals"></div>
    <h1 class="headline">What did you think of<br>this book?</h1>
    <div class="school-mark">Marrowby Lane School</div>
    <p class="pass-band">PLEASE PASS IT ON!</p>
    <p class="web-band">www.marrowbylane.sch.uk</p>
  </main>
</body>
</html>
```